Korvix App Graphics Design

Our application promotes location based self expression via pictures and text. The primary focus of the application is on the content posted and not on the person that posted it.

We want a very clean and fresh design that evokes positive energy. Our site is unique so our design should be as well. People will reveal thoughts on our site, so the design should convey a "revealing" feel. Our site is a place where people are comfortable to freely express themselves. Colors we have in mind are blue and green hues with earth tones for background.

Our project is to design ten screens for our Korvix application at resolution of 1136-by-640 pixels:

Feed Screen
Camera Screen
Post Screen
Check In Screen
Approval Screen
Map Screen
Flag Screen
Feed Select Screen
Export Screen
Menu Screen

In the contest phase we will require only three screens to be submitted. The screens we require to be submitted are: Feed Screen; Map Screen and Camera Screen. The designer we select as the winner of the competition will then complete the project and deliver a total of the ten screens described above in the handover phase.

We have attached a document below with detailed specs of each screen, we ask for your innovation to bring these screens to life through your design.
Updates

We want to clarify one aspect regarding the VISOR: the visor needs to be transparent so that when the picture scrolls underneath it, you can still see the picture underneath the visor.

Hi Everyone,

We have noticed that some designers need clarification regarding the visor element in the feed screen.
I have attached two examples to our brief area called:
Visor Example 1 and Visor Example 2

Please note that these are not the style we are looking for but are a good example to the concept of a Transparent Visor above the feed stream. We are looking for you guys to come up with a Visor concept that is consistent with the style of the design you are submitting.

Thanks,

Bo

Target Market(s)

People 17-40 who want to share their thought about the world around them.

Industry/Entity Type

Flag

Font styles to use
Sans Serif
Other font styles liked:
• We like “Helvetica New” or “Avenir” but are flexible

Requirements
Must have
• Visor component should look innovative.

```html
<!DOCTYPE html>
<html lang="en">
<head>
<meta charset="utf-8">
<title>Korvix – Approval Screen</title>
<link rel="stylesheet" href="https://fonts.googleapis.com/css2?family=Arimo:wght@400;700&display=swap">
<style>
  :root {
    --status-top: #f4f4f4;
    --status-bottom: #c9c9c9;
    --status-ink: #2b2b2b;
    --signal-blue: #1f6fd1;
    --battery-green: #3fc21f;
    --toolbar-top: #8a8a8a;
    --toolbar-bottom: #5a5a5a;
    --blue-light: #4f8fd6;
    --blue-mid: #2f6fbf;
    --blue-dark: #1f5aa8;
    --divider: #a9c8ec;
    --prompt-ink: #ffffff;
    --question-ink: #a8f0f0;
    --photo-sky: #8fc2e8;
    --photo-house: #d8d2c2;
    --photo-garden: #5f8f3a;
    --bottom-top: #6a6a6a;
    --bottom-bottom: #2e2e2e;
    --button-top: #ffb060;
    --button-mid: #f26a10;
    --button-bottom: #c94d00;
    --button-ink: #3a1a08;
  }
  * { box-sizing: border-box; margin: 0; padding: 0; }
  html, body { width: 676px; height: 1200px; overflow: hidden; background: #fff; }
  .screen {
    position: relative; width: 676px; height: 1200px; overflow: hidden;
    font-family: "Arimo", Arial, sans-serif;
  }
  .status-bar {
    position: absolute; left: 0; top: 0; width: 676px; height: 42px;
    background: linear-gradient(var(--status-top), var(--status-bottom));
  }
  .status-time {
    position: absolute; left: 0; right: 0; top: 8px; text-align: center;
    font-size: 25px; font-weight: 700; color: var(--status-ink);
  }
  .status-signal { position: absolute; left: 12px; top: 9px; }
  .status-battery { position: absolute; right: 14px; top: 11px; }
  .toolbar {
    position: absolute; left: 0; top: 42px; width: 676px; height: 148px;
    background: linear-gradient(#9a9a9a, var(--toolbar-top) 40%, var(--toolbar-bottom));
  }
  .prompt {
    position: absolute; left: 0; top: 190px; width: 676px; height: 159px;
    background: linear-gradient(var(--blue-mid), var(--blue-light) 50%, var(--blue-mid));
    border-bottom: 2px solid var(--divider);
    text-align: center;
  }
  .prompt-intro {
    margin: 26px auto 0; width: 520px;
    font-size: 18px; font-weight: 700; line-height: 22px; color: var(--prompt-ink);
  }
  .prompt-question {
    margin-top: 10px; font-size: 23px; font-weight: 700; color: var(--question-ink);
  }
  .post-panel {
    position: absolute; left: 0; top: 349px; width: 676px; height: 464px;
    background: linear-gradient(var(--blue-light), var(--blue-mid));
    border-bottom: 2px solid var(--divider);
  }
  .post-photo {
    position: absolute; left: 38px; top: 31px; width: 600px; height: 397px;
    border-radius: 12px;
    background: linear-gradient(var(--photo-sky) 0%, var(--photo-house) 35%, var(--photo-house) 70%, var(--photo-garden) 100%);
  }
  .text-area {
    position: absolute; left: 0; top: 813px; width: 676px; height: 228px;
    background: linear-gradient(var(--blue-mid), var(--blue-dark));
  }
  .post-text {
    position: absolute; left: 38px; top: 28px; width: 600px; height: 179px;
    border: 2px solid #7fb0e6; border-radius: 10px;
    background: linear-gradient(var(--blue-light), var(--blue-mid));
    padding: 26px 22px; color: #fff; font-size: 27px; line-height: 33px;
  }
  .action-bar {
    position: absolute; left: 0; top: 1041px; width: 676px; height: 159px;
    background: linear-gradient(var(--bottom-top), var(--bottom-bottom));
  }
  .action-button {
    position: absolute; top: 32px; width: 238px; height: 85px;
    border-radius: 10px; border: 2px solid #8a3a00;
    background: linear-gradient(var(--button-top), var(--button-mid) 45%, var(--button-bottom));
    box-shadow: inset 0 2px 0 rgba(255,255,255,.5);
    display: flex; align-items: center; justify-content: center; gap: 22px;
    font-size: 46px; font-weight: 700; color: var(--button-ink);
  }
  .action-yes { left: 38px; }
  .action-no { left: 401px; }
</style>
</head>
<body>
<main class="screen">
  <header class="status-bar">
    <svg class="status-signal" width="90" height="26" viewBox="0 0 90 26">
      <g fill="var(--signal-blue)">
        <rect x="0" y="16" width="5" height="9"/><rect x="7" y="12" width="5" height="13"/>
        <rect x="14" y="7" width="5" height="18"/><rect x="21" y="2" width="5" height="23"/>
        <path d="M58 25 l-5-6 a8 8 0 0 1 10 0z"/>
        <path d="M47 13 a16 16 0 0 1 22 0 l-3 3 a12 12 0 0 0-16 0z"/>
        <path d="M42 8 a23 23 0 0 1 32 0 l-3 3 a19 19 0 0 0-26 0z"/>
      </g>
    </svg>
    <div class="status-time">2:30</div>
    <svg class="status-battery" width="44" height="22" viewBox="0 0 44 22">
      <rect x="1" y="1" width="38" height="20" rx="3" fill="#fff" stroke="#333" stroke-width="2"/>
      <rect x="4" y="4" width="32" height="14" fill="var(--battery-green)"/>
      <rect x="40" y="7" width="3" height="8" fill="#333"/>
    </svg>
  </header>

  <div class="toolbar"></div>

  <section class="prompt">
    <p class="prompt-intro">To submit your post you must first moderate an anonymous post in your area</p>
    <p class="prompt-question">Is the following post appropoiate?</p>
  </section>

  <section class="post-panel">
    <div class="post-photo" role="img" aria-label="Photo of a modern white house with balconies and a garden"></div>
  </section>

  <section class="text-area">
    <p class="post-text">Lorem ipsum dolor sit amet consecteteur adipiscing elit, set diem nonumy in convalis gravida neque</p>
  </section>

  <footer class="action-bar">
    <div class="action-button action-yes">YES
      <svg width="36" height="36" viewBox="0 0 36 36"><rect width="36" height="36" rx="4" fill="var(--button-ink)"/><path d="M13 10 L25 18 L13 26z" fill="var(--button-mid)"/></svg>
    </div>
    <div class="action-button action-no">NO
      <svg width="36" height="36" viewBox="0 0 36 36"><rect width="36" height="36" rx="4" fill="var(--button-ink)"/><path d="M13 10 L25 18 L13 26z" fill="var(--button-mid)"/></svg>
    </div>
  </footer>
</main>
</body>
</html>
```